Webdesign for large cottage directory

We have developed a first version of a website that can accommodate large groups (10 to 300 people). The site is English and is aimed at a wide audience ranging from a group of students to a family or a family. For the visitors the site is free and it is the propietaires who pay to see their accommodation. The site is online with just a few fake lodgings and a simple design to the elements that must be appraised (nothing to keep the current design). Our website is here: lodgevista.com (login / pass = admin / 123) Home page (lodgevista.com): on this page section) and lodging by theme (third section). These three points should be highlighted as possible. The displayed map may be slightly modified. Only the background and the color changes when hovering over the mouse. It can be enlarged / retreciated. Below these 3 sections we have some fairly published articles, the latest blog posts and the footer. The menu will be visible throughout the site. Category page (https://lodgevista.fr/gite-departement/aveyron OR https://lodgevista.fr/gites-couchages-121): On these pages we always return the same format with the googlemap, an image 1 text. Below the list of the cottages concerned and the filter options. Product page: The pages presenting the cottages can be of two types: - Either the cottage has no owner and there is no contact for the visitor to the owner that he can retrieve his cottage by registering: example of a page of this type: https://lodgevista.fr/domaine-de-fressanac - The cottage to a propietaire and we are on the classic card. : // lodgevista. en / domain-of-fressanac2 For all products on the site we have nav tab. It's just for testing. We do not want to be in the design for real website. All information must be in the page without login / register page: classic, it's here: https://lodgevista.it/login and https://lodgevista.fr/register Blog homepage (https://lodgevista.fr/blog ): Classic blog page Blog post (https://lodgevista.fr/blog/urltemporaire1551521154) and static page (https://lodgevista.fr/blog/Systeme-classement-lodgevistafr): Nothing special Menu: Menu is an important part of the website. It's the way to navigate on the wbesite.
Faible participation designers
Number of Pages Required
4 page
Colors
Designer to choose colors to be used in the design.
Look and feel
Each slider illustrates characteristics of the customer's brand and the style your logo design should communicate.

```html
<!DOCTYPE html>
<html lang="fr">
<head>
<meta charset="utf-8">
<title>lodgevista.Fr — Gîtes de groupe</title>
<link href="https://fonts.googleapis.com/css2?family=Open+Sans:ital,wght@0,400;0,600;0,700;0,800;1,400&display=swap" rel="stylesheet">
<style>
:root{
  --blue:#1f5ef0;
  --blue-dark:#1548c4;
  --ink:#222428;
  --muted:#6b6f76;
  --line:#c7d3ef;
  --soft:#f4f5f8;
  --circle:#ececee;
  --footer:#121212;
  --footer-box:#2a2a2c;
  --white:#ffffff;
}
*{box-sizing:border-box;margin:0;padding:0}
html,body{width:1200px;height:5070px;overflow:hidden}
body{font-family:"Open Sans",Arial,sans-serif;color:var(--ink);background:var(--white)}

/* Header */
.site-header{height:75px;background:var(--blue);display:flex;align-items:center;padding:0 95px;position:relative}
.brand{color:var(--white);font-weight:800;font-size:26px;letter-spacing:-.3px}
.main-nav{position:absolute;left:430px;top:44px;display:flex;gap:26px}
.main-nav a{color:var(--white);font-size:14px;font-weight:600;text-decoration:none}
.account{position:absolute;right:45px;top:12px;display:flex;gap:12px}
.account a{background:var(--white);color:var(--blue);font-size:13px;font-weight:600;border-radius:14px;padding:4px 16px;text-decoration:none}

/* Section titles */
.section-title{display:flex;align-items:center;justify-content:center;gap:22px;font-size:32px;font-weight:700}
.section-title::before,.section-title::after{content:"";width:80px;height:2px;background:var(--line)}

/* Capacities */
.capacities{height:720px;padding-top:50px}
.capacity-grid{display:grid;grid-template-columns:repeat(3,355px);justify-content:center;row-gap:60px;margin-top:75px}
.capacity{text-align:center}
.capacity-circle{width:142px;height:142px;border-radius:50%;background:var(--circle);margin:0 auto;display:flex;align-items:center;justify-content:center;color:#9a9ca2;font-size:24px;font-weight:600}
.capacity-label{margin-top:24px;font-size:20px;font-weight:700;line-height:1.35;text-transform:uppercase}

/* Departments */
.departments{height:845px;padding-top:50px;background:var(--soft)}
.france-map{width:610px;height:645px;margin:55px auto 0;background:radial-gradient(circle at 50% 50%,#e4e6ea 0%,#d6d9de 70%,#eceef1 100%);border-radius:38% 42% 34% 40%}

/* Themes */
.themes{height:860px;padding-top:45px}
.theme-grid{display:grid;grid-template-columns:repeat(4,243px);gap:0 17px;justify-content:center;margin-top:30px}
.theme{height:251px}
.theme-photo{height:175px}
.theme-name{text-align:center;font-size:16px;font-weight:700;padding-top:18px}
.theme-name.active{color:var(--blue)}

/* About */
.about{height:627px;padding-top:80px}
.about-text{width:964px;margin:28px auto 0;text-align:center;font-size:14.5px;line-height:1.85;color:var(--muted)}
.about-text p+p{margin-top:20px}

/* Lodgings */
.lodgings{height:895px;padding-top:48px;background:var(--soft)}
.lodging-grid{display:grid;grid-template-columns:repeat(3,328px);gap:0 24px;justify-content:center;margin-top:20px}
.lodging{background:var(--white)}
.lodging-photo{height:250px}
.lodging-body{padding:16px 14px 0;font-size:14px;line-height:1.6;height:375px}
.lodging-body h3{font-size:15px;font-weight:700;margin-bottom:6px}
.lodging-body p{margin-bottom:8px}
.lodging-body b{font-weight:700}
.tags{display:flex;gap:5px;margin-bottom:8px}
.tag{background:var(--blue);color:var(--white);font-size:9.5px;padding:1px 6px;border-radius:2px}
.fav-button{display:block;background:var(--blue);color:var(--white);text-align:center;font-size:15px;font-weight:700;height:40px;line-height:40px;margin-top:3px}

/* Blog */
.blog{height:524px;padding-top:35px;position:relative}
.blog-grid{display:grid;grid-template-columns:repeat(4,236px);gap:0 24px;justify-content:center;margin-top:22px}
.post{background:var(--soft);height:365px}
.post-photo{height:173px}
.post h3{font-size:15px;font-weight:700;padding:16px 14px 6px}
.post p{font-size:11px;line-height:1.55;color:var(--muted);padding:0 14px}
.arrow{position:absolute;top:252px;width:18px;height:18px}
.arrow.prev{left:52px}.arrow.next{right:45px}

/* Footer */
.site-footer{height:456px;background:var(--footer);color:var(--white);position:relative}
.footer-brand{position:absolute;left:95px;top:90px;width:230px}
.footer-brand .brand{font-size:28px}
.footer-brand p{font-style:italic;font-size:13.5px;line-height:1.55;margin-top:12px}
.footer-col{position:absolute;top:92px}
.footer-col h4{font-size:14px;font-weight:700;padding-bottom:6px;border-bottom:2px solid var(--white);display:inline-block;margin-bottom:10px}
.footer-col li{list-style:none;font-size:12.5px;line-height:1.6}
.col-capacity{left:355px}.col-theme{left:625px}
.newsletter{position:absolute;left:888px;top:84px;width:262px;height:216px;background:var(--footer-box);text-align:center;padding-top:22px}
.newsletter h4{font-size:20px;font-weight:700;color:#5a5a5e;line-height:1.3;margin-top:8px}
.newsletter .email{width:200px;height:36px;background:var(--white);margin:14px auto 0;text-align:left;color:#999;font-size:13px;padding:8px 12px}
.newsletter .subscribe{width:200px;height:36px;background:var(--blue);border-radius:18px;margin:12px auto 0;font-size:15px;font-weight:700;line-height:36px}
.socials{position:absolute;left:922px;top:352px;display:flex;gap:12px}
.socials span{width:34px;height:34px;border-radius:50%;background:var(--white)}
.copyright{height:68px;background:var(--footer);border-top:1px solid #2c2c2c;text-align:center;color:var(--white);font-size:14px;line-height:68px}
.copyright b{color:var(--blue);font-weight:600}
</style>
</head>
<body>

<header class="site-header">
  <div class="brand">lodgevista.Fr</div>
  <nav class="main-nav">
    <a href="#">Gîte par capacité ▾</a>
    <a href="#">Gîte par département ▾</a>
    <a href="#">Gîte par thématique ▾</a>
    <a href="#">Blog</a>
    <a href="#">Vos favoris</a>
  </nav>
  <div class="account"><a href="#">Connexion</a><a href="#">S'enregistrer</a></div>
</header>

<section class="capacities">
  <h2 class="section-title">Gîtes par Capacités</h2>
  <div class="capacity-grid">
    <div class="capacity"><div class="capacity-circle">10 to 50</div><div class="capacity-label">10 à 50<br>personnes</div></div>
    <div class="capacity"><div class="capacity-circle">50 to 100</div><div class="capacity-label">50 à 100<br>personnes</div></div>
    <div class="capacity"><div class="capacity-circle">100 to 150</div><div class="capacity-label">100 à 150<br>personnes</div></div>
    <div class="capacity"><div class="capacity-circle">150 to 200</div><div class="capacity-label">150 à 200<br>personnes</div></div>
    <div class="capacity"><div class="capacity-circle">200 to 250</div><div class="capacity-label">200 à 250<br>personnes</div></div>
    <div class="capacity"><div class="capacity-circle">250 to 300</div><div class="capacity-label">250 à 300<br>personnes</div></div>
  </div>
</section>

<section class="departments">
  <h2 class="section-title">Gîtes par Departement</h2>
  <div class="france-map" role="img" aria-label="Carte de France découpée par départements"></div>
</section>

<section class="themes">
  <h2 class="section-title">Gîtes par Thématique</h2>
  <div class="theme-grid">
    <div class="theme"><div class="theme-photo" role="img" aria-label="Photo séminaire, tons bleus" style="background:linear-gradient(135deg,#1b4fd0,#2b6ae8)"></div><div class="theme-name active">Séminaire</div></div>
    <div class="theme"><div class="theme-photo" role="img" aria-label="Photo de pêches" style="background:linear-gradient(135deg,#e0823a,#7a3a1c)"></div><div class="theme-name">Pêche</div></div>
    <div class="theme"><div class="theme-photo" role="img" aria-label="Photo de moto" style="background:linear-gradient(135deg,#8a6b52,#3d2f26)"></div><div class="theme-name">Motorcycles</div></div>
    <div class="theme"><div class="theme-photo" role="img" aria-label="Photo de plongée sous-marine" style="background:linear-gradient(135deg,#1f6f86,#0f3a4c)"></div><div class="theme-name">Aquatique</div></div>
    <div class="theme"><div class="theme-photo" role="img" aria-label="Photo d'équitation" style="background:linear-gradient(135deg,#a3b6c6,#4c5d6c)"></div><div class="theme-name">Equitation</div></div>
    <div class="theme"><div class="theme-photo" role="img" aria-label="Photo de montagne enneigée" style="background:linear-gradient(180deg,#9fc3e4,#eef3f8)"></div><div class="theme-name">Neige</div></div>
    <div class="theme"><div class="theme-photo" role="img" aria-label="Photo d'une classe en plein air" style="background:linear-gradient(135deg,#d8d2c8,#3a3430)"></div><div class="theme-name">Classe Transplantée</div></div>
    <div class="theme"><div class="theme-photo" role="img" aria-label="Photo de VTT en forêt" style="background:linear-gradient(135deg,#5b6e3e,#1f2a1a)"></div><div class="theme-name">VTT</div></div>
    <div class="theme"><div class="theme-photo" role="img" aria-label="Photo de plat gastronomique" style="background:linear-gradient(135deg,#5a3b30,#1d1413)"></div><div class="theme-name">Gastronomique</div></div>
    <div class="theme"><div class="theme-photo" role="img" aria-label="Photo de randonnée en nature" style="background:linear-gradient(135deg,#c99a6b,#5e4a3a)"></div><div class="theme-name">Nature et randonnée</div></div>
    <div class="theme"><div class="theme-photo" role="img" aria-label="Photo de colonie de vacances" style="background:linear-gradient(135deg,#e2b27a,#6d5542)"></div><div class="theme-name">Colonie de vacances</div></div>
    <div class="theme"><div class="theme-photo" role="img" aria-label="Photo de café et gâteau" style="background:linear-gradient(135deg,#e8dfd4,#8a5a3e)"></div><div class="theme-name">week-end d'integration</div></div>
  </div>
</section>

<section class="about">
  <h2 class="section-title">Notre site</h2>
  <div class="about-text">
    <p>Lorem ipsum dolor sit amet, consectetur adipiscing elit. Laughter bowl takes one set of products. Donec ultrices metus sit amet molestie dignissim. That they in the arcu lacinia iaculis Vivamus vitae eleifend tortor sit amet felis. Integer indicates that entrepreneurs skirt impact. Let us live by bow and lorem element, it need lorem ut. Nulla School of Medicine, said that various carrots invest will disappear. For the basketball from door to the casino. Until and use, no for. The carrot soccer competition, Metro basketball and football. Until it passes gos. The ends of the Dus lorem urna. There is no pill now Pakistan, and the protein is always one upper.</p>
    <p>Before the very first basketball set their jaws greet and clinical care. It's just the region but basketball, a list of the valley just bananas. Planning queue at mass manufacturing environment. Vestibulum vitae egestas nulla, luctus felis a nunc. Each time the urn, one that bows Planning team. Sed consectetur television from the arc. Nunc was among members of a slide, running up to now. The life of the mass of Eucalisa aliquet suscipit tortor, eu mollis risus euismod. Clinical carrots drink worth it. But no quiver laughter. Pellentesque sterilised weekend. Phasellus pulvinar the bed is brought about by any of life, eu mattis magna placerat.</p>
    <p>As a graduated shafts, members of carrots, skirt ugly. Performance football soft smile. Clinical carrots drink worth it. But no quiver laughter. Pellentesque sterilised weekend. Phasellus pulvinar the bed is brought about by any of life, eu mattis magna placerat. As a graduated shafts, members of carrots, skirt ugly. Performance football soft smile. Clinical carrots drink worth it. But no quiver laughter. Pellentesque sterilised weekend. Phasellus pulvinar the bed is brought about by any of life, eu mattis magna placerat. As a graduated shafts, members of carrots, skirt ugly.</p>
  </div>
</section>

<section class="lodgings">
  <h2 class="section-title">Last 10 lodgings added</h2>
  <div class="lodging-grid">
    <article class="lodging">
      <div class="lodging-photo" role="img" aria-label="Photo de voyageur au soleil" style="background:linear-gradient(135deg,#d9a35c,#6b4a2c)"></div>
      <div class="lodging-body">
        <h3>What is Lorem Ipsum?</h3>
        <p><b>Adresse:</b> 27 Rue des Tilleuls, 75011 Paris, France</p>
        <p><b>Region :</b> Occitanie<br><b>Departement :</b> Aveyron<br><b>Capacité :</b> 13</p>
        <p><b>Formule Proposée:</b> Gestion libre, Pension complète, Nuitée seule</p>
        <div class="tags"><span class="tag">Salle de réception</span><span class="tag">Piscine</span><span class="tag">Cuisine professionnelle</span></div>
        <p><b>description:</b> Qu'est-ce que le Lorem Ipsum? Le Lorem Ipsum est simplement du faux texte employé dans la...</p>
        <a class="fav-button" href="#">AJOUTER AUX FAVORIS</a>
      </div>
    </article>
    <article class="lodging">
      <div class="lodging-photo" role="img" aria-label="Photo de tasse de café sur une table" style="background:linear-gradient(135deg,#e6e1da,#8c7f72)"></div>
      <div class="lodging-body">
        <h3>What is Lorem Ipsum?</h3>
        <p><b>Adresse:</b> 27 Rue des Tilleuls, 75011 Paris, France</p>
        <p><b>Region :</b> Occitanie<br><b>Departement :</b> Aveyron<br><b>Capacité :</b> 13</p>
        <p><b>Formule Proposée:</b> Gestion libre, Pension complète, Nuitée seule</p>
        <div class="tags"><span class="tag">Salle de réception</span><span class="tag">Piscine</span><span class="tag">Cuisine professionnelle</span></div>
        <p><b>description:</b> Qu'est-ce que le Lorem Ipsum? Le Lorem Ipsum est simplement du faux texte employé dans la...</p>
        <a class="fav-button" href="#">AJOUTER AUX FAVORIS</a>
      </div>
    </article>
    <article class="lodging">
      <div class="lodging-photo" role="img" aria-label="Photo de montagne rocheuse sous ciel bleu" style="background:linear-gradient(180deg,#5fa6d8,#8a7564)"></div>
      <div class="lodging-body">
        <h3>What is Lorem Ipsum?</h3>
        <p><b>Adresse:</b> 27 Rue des Tilleuls, 75011 Paris, France</p>
        <p><b>Region :</b> Occitanie<br><b>Departement :</b> Aveyron<br><b>Capacité :</b> 13</p>
        <p><b>Formule Proposée:</b> Gestion libre, Pension complète, Nuitée seule</p>
        <div class="tags"><span class="tag">Salle de réception</span><span class="tag">Piscine</span><span class="tag">Cuisine professionnelle</span></div>
        <p><b>description:</b> Qu'est-ce que le Lorem Ipsum? Le Lorem Ipsum est simplement du faux texte employé dans la...</p>
        <a class="fav-button" href="#">AJOUTER AUX FAVORIS</a>
      </div>
    </article>
  </div>
</section>

<section class="blog">
  <h2 class="section-title">Derniers articles du Blog</h2>
  <svg class="arrow prev" viewBox="0 0 18 18"><path d="M12 3 6 9l6 6" fill="none" stroke="#222" stroke-width="2"/></svg>
  <svg class="arrow next" viewBox="0 0 18 18"><path d="m6 3 6 6-6 6" fill="none" stroke="#222" stroke-width="2"/></svg>
  <div class="blog-grid">
    <article class="post"><div class="post-photo" role="img" aria-label="Photo de paysage polaire" style="background:linear-gradient(180deg,#7fa9c9,#dfe7ee)"></div><h3>Why do we use it</h3><p>Lorem Ipsum is simply dummy text of the printing and typesetting industry. Lorem Ipsum has been the industry's standard dummy text ever since the 1500s, when an unknown printer took a galley of type and scrambled it to make a type specimen book. It has survived not only five centuries.</p></article>
    <article class="post"><div class="post-photo" role="img" aria-label="Photo de montagnes au crépuscule" style="background:linear-gradient(180deg,#3c5a7a,#2a2a30)"></div><h3>Why do we use it</h3><p>Lorem Ipsum is simply dummy text of the printing and typesetting industry. Lorem Ipsum has been the industry's standard dummy text ever since the 1500s, when an unknown printer took a galley of type and scrambled it to make a type specimen book. It has survived not only five centuries.</p></article>
    <article class="post"><div class="post-photo" role="img" aria-label="Photo de vallée verte et montagne" style="background:linear-gradient(180deg,#9cc3d8,#3f6a4a)"></div><h3>Why do we use it</h3><p>Lorem Ipsum is simply dummy text of the printing and typesetting industry. Lorem Ipsum has been the industry's standard dummy text ever since the 1500s, when an unknown printer took a galley of type and scrambled it to make a type specimen book. It has survived not only five centuries.</p></article>
    <article class="post"><div class="post-photo" role="img" aria-label="Photo d'une conférence sur scène" style="background:linear-gradient(135deg,#2a3550,#0f1320)"></div><h3>Why do we use it</h3><p>Lorem Ipsum is simply dummy text of the printing and typesetting industry. Lorem Ipsum has been the industry's standard dummy text ever since the 1500s, when an unknown printer took a galley of type and scrambled it to make a type specimen book. It has survived not only five centuries.</p></article>
  </div>
</section>

<footer class="site-footer">
  <div class="footer-brand">
    <div class="brand">lodgevista.Fr</div>
    <p>Lorem Ipsum is simply dummy text of the printing and typesetting industry. Lorem Ipsum has been the industry's standard dummy text ever since the 1500s, when an unknown printer took a galley of type and scrambled it to make a type specimen book. It has survived not only five centuries.</p>
  </div>
  <div class="footer-col col-capacity">
    <h4>Lodging by capacity</h4>
    <ul><li>- 10 to 50 People</li><li>- 50 to 100 People</li><li>- 100 to 150 People</li><li>- 150 to 200 People</li><li>- 200 to 250 People</li><li>- 250 to 300 People</li></ul>
  </div>
  <div class="footer-col col-theme">
    <h4>Lodging by Theme</h4>
    <ul><li>- Seminar</li><li>- Peach</li><li>- Motorcycles</li><li>- Aquatique</li><li>- Equitation</li><li>- Neige</li><li>- Classe Transplantée</li><li>- vtt</li><li>- Gastronomique</li><li>- Nature et Randonnée</li><li>- Colonie de Vacances</li><li>- week-end d'integration</li></ul>
  </div>
  <div class="newsletter">
    <svg width="26" height="20" viewBox="0 0 26 20"><rect x="1" y="1" width="24" height="18" fill="none" stroke="#1f5ef0" stroke-width="2"/><path d="m1 1 12 10L25 1" fill="none" stroke="#1f5ef0" stroke-width="2"/></svg>
    <h4>Subscribe to<br>Newsletter</h4>
    <div class="email">Email</div>
    <div class="subscribe">SUBSCRIBE</div>
  </div>
  <div class="socials"><span></span><span></span><span></span><span></span></div>
</footer>
<div class="copyright">© Copyrights 2019 <b>lodgevista.Fr</b>. All rights reserved</div>

</body>
</html>
```